CBD Boutique Business Card Needed

We are in need of a business card to reflect the direction of our latest products. We are a fully organic company in which our store and products are very heavy in wood and "natural" components. We decided to bring color into one of our brands and immediately knew this is where we needed to go.

We are NOT a cash grab CBD company. We could have done this wrong, slapped a label on a shit product and left it like that. I am passionate about sharing my experience with other veterans and opening a store and making it a comfortable place for others to come and see if they can have the same experience.

Target Market(s)

We are a dual market company. We do have a beauty line that will cover the costs of the majority of our business. But we also heavily cater to veterans and first responders. I am a veteran and this is how I found out about CBD. So the marketing needs to bring in our higher end beauty clientele but also be able to not put off our customers that readily need this.

Contact Information for Business Card

What we are looking for is a light, professional, boutique design that is is neither quite feminine or masculine. Attached is a picture of a store in Portland that we asked our store designer to get her inspiration from. But all natural wood and black outlines are what is mostly in there.

Attached are the following files:

Logo: An AI file with how we have our logo. I do not understand AI and have no idea why the letters are individual. The font is Adam. OLU is the logo and Tonics of Vigor is our tagline.

KM Vantage (front and back) cards I did originally found at a trade show that I absolutely loved...while it is mostly there and I would still be happy with them but it is me pretending to be you. I understand I am not and there is probably a lot wrong that all of you would see instantly and this is why I am here.

Dropper Bottle: This is our final product mock up

Water Color: I am semi flexible here. This water color is slightly different on every level of our brand. The color itself can change...we are not stuck on THIS particular one. If you happen to make a new one that is similar in style and we use it...then I will happily commission you to change the rest on our next product run. I am pretty sure you can use this statement as evidence later . =) .

But seriously, we heavily believe in pay it forward and will work with anyone here that may have a vision bigger than ours. The winner of this contest will get preferential consideration on our marketing materials (need letterhead etc. next, as well as a brochure, and website) so three more projects coming down the pipeline.

Information to use for your mockup is contained on the card images I have included. I would prefer CBD for wellness CBD for life to be more prominent. No where else on the card do we have CBD mentioned.

Font styles to use
Sans Serif

Colors

Designer to choose colors to be used in the design.

Requirements
Must have
• Double Sided
• Front: OLU logo on front of card will be raised embossed. Background is watercolor. One has been provided. Others are up for consideration. If the rest of your design is incredible and I don't like your watercolor I will just ask to swap it.
• Back: Standard information. Not stuck on anything here. I LOVE clean minimal designs. The bleed on the card I provided is a luxury...
• Font for title and OLU is Adam. Everything else I prefer san serif or as clean as possible.
Nice to have
• I Need to incorporate Naturally Nurturing somewhere on the card. Bold but not intrusive.

```html
<!DOCTYPE html>
<html lang="en">
<head>
<meta charset="utf-8">
<title>OLU – Tonics of Vigor Business Card</title>
<link rel="stylesheet" href="https://fonts.googleapis.com/css2?family=Open+Sans:wght@300;400;700&display=swap">
<style>
  :root {
    --backdrop: #d6d6d6;
    --wash-aqua: #3fb6dd;
    --wash-sky: #8fd3ea;
    --wash-mist: #c9e9f3;
    --wash-lilac: #c7a6d3;
    --wash-violet: #9a88c9;
    --ink: #111417;
    --paper-white: #ffffff;
  }
  * { box-sizing: border-box; margin: 0; padding: 0; }
  html, body {
    width: 1200px; height: 800px; overflow: hidden;
    background: var(--backdrop);
    font-family: "Open Sans", Arial, sans-serif;
  }
  .canvas {
    width: 1200px; height: 800px;
    display: flex; align-items: center; justify-content: center; gap: 40px;
  }
  .card {
    position: relative;
    width: 540px; height: 309px;
    overflow: hidden;
    box-shadow: 0 6px 16px rgba(0,0,0,0.18);
  }
  .card__wash {
    position: absolute; inset: 0;
    background:
      radial-gradient(ellipse 55% 45% at 78% 18%, var(--wash-lilac) 0%, transparent 70%),
      radial-gradient(ellipse 45% 40% at 12% 85%, var(--wash-violet) 0%, transparent 70%),
      radial-gradient(ellipse 60% 55% at 45% 45%, var(--wash-mist) 0%, transparent 75%),
      radial-gradient(ellipse 50% 50% at 85% 85%, var(--wash-aqua) 0%, transparent 75%),
      linear-gradient(135deg, var(--wash-sky), var(--wash-aqua) 55%, var(--wash-sky));
  }

  /* Front */
  .front__brand {
    position: absolute; left: 0; right: 0; top: 92px;
    text-align: center; color: var(--paper-white);
  }
  .front__name {
    font-weight: 300; font-size: 84px; line-height: 1; letter-spacing: 6px;
  }
  .front__tagline {
    margin-top: 10px;
    font-weight: 300; font-size: 20px; letter-spacing: 3px; text-transform: uppercase;
  }

  /* Back */
  .back__brand {
    position: absolute; top: 34px; right: 96px;
    text-align: center; color: var(--ink);
  }
  .back__name { font-weight: 300; font-size: 50px; line-height: 1; letter-spacing: 4px; }
  .back__tagline { margin-top: 4px; font-weight: 300; font-size: 12px; letter-spacing: 1.5px; text-transform: uppercase; }
  .back__rule {
    position: absolute; top: 115px; left: 160px; right: 52px;
    height: 1px; background: var(--ink);
  }
  .back__address {
    position: absolute; top: 130px; right: 52px;
    text-align: right; font-size: 12px; line-height: 1.35; color: var(--ink);
  }
  .back__person { position: absolute; left: 40px; top: 188px; color: var(--ink); }
  .person__name { font-weight: 700; font-size: 15px; letter-spacing: 0.5px; }
  .person__title { font-size: 12px; margin-left: 12px; }
  .person__rule { width: 230px; height: 1px; background: var(--ink); margin-top: 6px; }
  .contact-list {
    list-style: none; position: absolute; left: 52px; top: 248px;
    font-size: 12px; line-height: 16px; color: var(--ink);
  }
  .contact-list li { display: flex; align-items: center; gap: 8px; }
  .contact-list svg { width: 11px; height: 11px; fill: var(--ink); }
</style>
</head>
<body>
<main class="canvas">

  <section class="card card--front">
    <div class="card__wash" role="img" aria-label="Soft blue and lilac watercolor wash background"></div>
    <div class="front__brand">
      <div class="front__name">OLU</div>
      <div class="front__tagline">Tonics of Vigor</div>
    </div>
  </section>

  <section class="card card--back">
    <div class="card__wash" role="img" aria-label="Soft blue and lilac watercolor wash background"></div>
    <div class="back__brand">
      <div class="back__name">OLU</div>
      <div class="back__tagline">Tonics of Vigor</div>
    </div>
    <div class="back__rule"></div>
    <p class="back__address">Your address, city<br>state, ZIP 0000</p>

    <div class="back__person">
      <div class="person__name">YOUR NAME</div>
      <div class="person__title">Your Title</div>
      <div class="person__rule"></div>
    </div>

    <ul class="contact-list">
      <li>
        <svg viewBox="0 0 24 24" aria-hidden="true"><path d="M6.6 10.8a15.1 15.1 0 0 0 6.6 6.6l2.2-2.2a1 1 0 0 1 1-.25 11.4 11.4 0 0 0 3.6.57 1 1 0 0 1 1 1V20a1 1 0 0 1-1 1A17 17 0 0 1 3 4a1 1 0 0 1 1-1h3.5a1 1 0 0 1 1 1c0 1.25.2 2.45.57 3.57a1 1 0 0 1-.25 1z"/></svg>
        <span>123-456-2100</span>
      </li>
      <li>
        <svg viewBox="0 0 24 24" aria-hidden="true"><path d="M2 5h20v14H2z M3.5 6.5 12 13l8.5-6.5" fill="none" stroke="#111417" stroke-width="2"/></svg>
        <span>youremail@mailhub.com</span>
      </li>
      <li>
        <svg viewBox="0 0 24 24" aria-hidden="true"><circle cx="12" cy="12" r="10" fill="none" stroke="#111417" stroke-width="2"/><path d="M2 12h20M12 2c3 3 3 17 0 20M12 2c-3 3-3 17 0 20" fill="none" stroke="#111417" stroke-width="1.6"/></svg>
        <span>www.yourwebsite.com</span>
      </li>
    </ul>
  </section>

</main>
</body>
</html>
```